Health Education Non-Profit Needs a Designer to Layout Magazine (Contest)

Hello, we are looking for someone to layout our print magazine. We'd like to work with someone who also has graphic design experience manipulating photos (see 2 sample issue links below for examples). Ad design is also needed. We like the current design of our magazine, so we are hoping our next designer can maintain the same look and feel as our previous magazines. Samples of our past two issues can be found at https://www.qelmarhub.org/wp-content/uploads/2019/03/issue-09-feb-2019.pdf and https://www.qelmarhub.org/wp-content/uploads/2018/11/the-spruce-courier-2018-05-issue-08.pdf

There are typically 2-4 different issues per year with around 11 articles in each issue. Issues are 24 pages. If there is a lot of white space, we may ask the designer to design an ad at the end of the article. We are looking to work with someone who is responsive and has a quick turnaround time (e.g., takes around 3 weeks to design the entire issue).

For this contest, please design a cover and article. Please refer to our last two issues (links above) before designing. We would like to see how the designer can take the images and edit them in a way that incorporates them seamlessly into the magazine as has been done in the past. Our end goal will be for the designer to design the entire issue and future issues. We anticipate this contest will not cover the entire cost of the work for completing the issue. When we find a designer we like, we will work out details for additional payment. Images can be found here: https://files.travonbox.net/folders/7QpRw2ZkLmX9vTn4aYc6Hs0bEjUdF3gK?usp=sharing

```html
<!DOCTYPE html>
<html lang="en">
<head>
<meta charset="utf-8">
<title>Caregiving Together – Article Page</title>
<link href="https://fonts.googleapis.com/css2?family=Noto+Serif:ital,wght@0,400;0,700;1,400&display=swap" rel="stylesheet">
<style>
  :root {
    --paper: #ebe8e3;
    --ink: #2a3532;
    --heading: #1d3b33;
    --photo-top-a: #6f8a86;
    --photo-top-b: #c9c6bf;
    --photo-bottom-a: #8e9aa6;
    --photo-bottom-b: #3a4a66;
  }
  html, body {
    margin: 0;
    padding: 0;
    width: 927px;
    height: 1200px;
    overflow: hidden;
    background: var(--paper);
  }
  .page {
    position: relative;
    width: 927px;
    height: 1200px;
    background: var(--paper);
    font-family: "Noto Serif", Georgia, serif;
    color: var(--ink);
    font-size: 15.4px;
    line-height: 21.8px;
    overflow: hidden;
  }
  .photo {
    position: absolute;
  }
  .photo--consult {
    left: 0;
    top: 0;
    width: 465px;
    height: 343px;
    background: linear-gradient(160deg, var(--photo-top-b) 0%, #9fb1ae 35%, var(--photo-top-a) 70%, #55706b 100%);
  }
  .photo--walk {
    right: 0;
    bottom: 0;
    width: 360px;
    height: 465px;
    background:
      linear-gradient(90deg, var(--paper) 0%, rgba(235,232,227,0) 40%),
      linear-gradient(180deg, rgba(235,232,227,0) 0%, #c8ccd0 30%, var(--photo-bottom-a) 60%, var(--photo-bottom-b) 100%);
  }
  .column {
    position: absolute;
    width: 428px;
  }
  .column--left { left: 28px; top: 358px; }
  .column--right { left: 473px; top: 48px; width: 430px; }
  .column p { margin: 0 0 21.8px 0; }
  .lead { font-weight: 700; color: var(--heading); }
  .byline {
    position: absolute;
    left: 473px;
    top: 765px;
    width: 320px;
    font-size: 10.6px;
    line-height: 14.6px;
    font-style: italic;
    color: var(--ink);
    margin: 0;
  }
  .byline-spacer { float: right; width: 0; height: 58px; }
  .byline-notch { float: right; clear: right; width: 168px; height: 120px; }
</style>
</head>
<body>
<main class="page">
  <div class="photo photo--consult" role="img" aria-label="Photo of a couple meeting with a counselor holding a clipboard"></div>
  <div class="photo photo--walk" role="img" aria-label="Photo of a smiling woman using a walker beside a young man outdoors"></div>

  <section class="column column--left">
    <p><span class="lead">Communication is key (and it’s okay if you need help with it).</span> No matter what your pre-existing relationship is like, you and your caregiver need “open, clear, and quite intimate communication on both sides,” Varnholt says. Remember that you’re in it together, especially during times of stress or conflict.</p>
    <p>“If there’s a disagreement, the first thing to do is have a conversation and really listen to each other. Try not to blame,” says Varnholt. “Do a lot of listening and reflecting back: ‘If I heard you correctly, this is what I’m hearing, is that right?’ And then, you can problem-solve effectively as a team.”</p>
    <p>If you’re struggling to do this on your own, psychologists, social workers and other mediators can clarify the problem and identify a resolution. Your psychologist or social worker may be especially helpful if disagreement involves adherence to your prescribed treatment regimen, which is a frequent source of conflict among people on dialysis and their loved ones. “If noncompliance is an issue, as a psychologist, I want to know the context,” Varnholt says. “Aspects of dialysis may be uncomfortable, painful, expensive, inconvenient, or sad, but these things can often be ameliorated. Together, we can all identify the source of the problem, and then find a way to resolve it.”</p>
    <p><span class="lead">For caregivers, feeling overwhelmed and having feelings such as guilt or frustration are understandable and normal,</span> says Dressler.</p>
    <p>“It’s a big change to take on an unexpected role,” she says. “It can be helpful for them to know it is common for caregivers to feel this way. It can also be helpful to encourage them to have open communication to express these feelings.”</p>
  </section>

  <section class="column column--right">
    <p>Dressler also suggests that caregivers rely on the medical team, other family members and friends for support. “If the caregiver takes sole responsibility for everything, [he/she will] get burned out,” she cautions. Other ways to prevent caregiver burnout include active self-care—like eating well, getting enough sleep and exercising—and keeping a consistent schedule, according to Varnholt.</p>
    <p>“When your lives are routinized, you know what to expect and there’s less stress of the unknown,” Varnholt says. “Remember to make time for yourself—and find reasons to laugh.”</p>
    <p>She also suggests that caregivers learn “as much as possible about the medical situation and what dialysis is like, and write it down so you can refer to it when you’re feeling overwhelmed,” she says.</p>
    <p><span class="lead">Your relationship may grow even stronger.</span> You will undoubtedly face both physical and emotional challenges while on dialysis, no matter your prognosis. But patients and caregivers often become deeply bonded, and Varnholt and Dressler say that you have the opportunity for growth and even joy through this ordeal.</p>
    <p>“These challenging situations can actually bring people closer together,” says Dressler. “Patients and caregivers may experience a shift in values after both evaluating what’s truly important in their lives, they may prioritize things in a new way together.”</p>
  </section>

  <p class="byline"><span class="byline-spacer"></span><span class="byline-notch"></span>Mirela Tansey is a writer and editor at the Northfield Behavioral Society. This resource was developed jointly by the Northfield Behavioral Society and Qelmar Hub Citizens Education Center as part of a partnership to educate dialysis patients and their families on the psychological and emotional aspects of managing kidney disease.</p>
</main>
</body>
</html>
```